Redesign of existing site - Velbrin GmbH

Redesign of the following site.
https://www.velbrin-gmbh.example/

The colors red and green need to remain.
Topic: calendar binder

The font "FF Market Regular" should be used s well. But -- if you find a font which is similar and a bit more modern, then go with it. (see font-example.jpg)

The mainpage should have a slider with a video first. Enclosed is a screenshot of the video. (see video.jpg)

Logo also enclosed as svg. The red color might not be quit right. Please check it on your own.
For the second page this page should be used to redesign:
https://www.velbrin-gmbh.example/bindungen/ring-wire-bindung/

I am planing to use the DIVI builder. If you built this in DIVI builder and be able to send me the template or installation (Duplicator) that would be a huge advantage.
Updates

IMPORTANT:
I have received many designs in English. But I can't present them to the customer. Please convert them into German, otherwise they cannot be used.

Requirements
Must have
• Please translate designs into german if it is to be considered. How should I explain a design in english to the customer?

```html
<!DOCTYPE html>
<html lang="de">
<head>
<meta charset="utf-8">
<title>Velbrin GmbH – Startseite</title>
<link rel="stylesheet" href="https://fonts.googleapis.com/css2?family=Mulish:wght@400;600;700;800&family=Merriweather:wght@400;700&family=Caveat:wght@600&display=swap">
<style>
  :root {
    --accent: #f0676f;
    --accent-soft: #f47a80;
    --brand-red: #e3262d;
    --ink: #2b2b2b;
    --muted: #6f6f6f;
    --line: #e9e9e9;
    --field-border: #e2e2e2;
    --white: #ffffff;
    --hero-left: #dde4d8;
    --hero-mid: #e9ece6;
    --hero-right: #eef0f4;
    --cover: #a3286a;
  }
  * { box-sizing: border-box; margin: 0; padding: 0; }
  html, body { width: 1200px; height: 839px; overflow: hidden; background: var(--white); }
  body { position: relative; font-family: "Mulish", Arial, sans-serif; color: var(--ink); }

  .site-header { position: absolute; left: 0; top: 0; width: 1200px; height: 108px; background: var(--white); }
  .brand { position: absolute; left: 74px; top: 37px; font-family: "Mulish", Arial, sans-serif; font-weight: 800; font-size: 27px; letter-spacing: -0.5px; color: var(--brand-red); line-height: 1; }
  .main-nav { position: absolute; top: 46px; left: 396px; display: flex; gap: 26px; font-size: 14px; font-weight: 600; }
  .main-nav a { white-space: nowrap; color: var(--ink); text-decoration: none; letter-spacing: 0.2px; }
  .main-nav a.is-active { color: var(--accent); border-bottom: 1px solid var(--accent); padding-bottom: 4px; }
  .main-nav .caret { font-size: 8px; margin-left: 4px; vertical-align: 2px; }
  .header-tools { position: absolute; top: 46px; left: 0; }
  .tool { position: absolute; width: 20px; height: 20px; }
  .tool-count { position: absolute; width: 22px; height: 22px; border-radius: 50%; background: var(--accent); color: var(--white); font-size: 12px; font-weight: 700; text-align: center; line-height: 22px; }

  .hero { position: absolute; left: 0; top: 109px; width: 1200px; height: 436px; overflow: hidden; }
  .hero-photo { position: absolute; inset: 0; background: linear-gradient(90deg, var(--hero-left) 0%, var(--hero-mid) 40%, var(--hero-right) 100%); }
  .hero-product { position: absolute; left: 492px; top: 0; width: 452px; height: 436px; background: linear-gradient(100deg, #e7c9c0 0%, #efe9e4 30%, #c84c8a 60%, var(--cover) 100%); opacity: 0.55; border-radius: 0 0 40px 40px; }
  .hero-kicker { position: absolute; left: 140px; top: 157px; font-size: 13px; color: var(--accent); }
  .hero-title { position: absolute; left: 140px; top: 176px; font-family: "Caveat", cursive; font-weight: 600; font-size: 35px; line-height: 33px; color: #1f1f1f; }
  .hero-cta { position: absolute; left: 140px; top: 262px; width: 166px; height: 39px; background: var(--accent-soft); color: var(--white); font-size: 14px; font-weight: 700; text-align: center; line-height: 39px; }
  .slider-dots { position: absolute; top: 498px; left: 576px; display: flex; gap: 10px; }
  .slider-dots span { width: 11px; height: 11px; border-radius: 50%; background: rgba(255,255,255,0.75); }
  .slider-dots span.is-current { background: var(--accent); }

  .features { position: absolute; top: 586px; left: 0; width: 1200px; }
  .feature { position: absolute; width: 320px; }
  .feature-icon { position: absolute; left: 0; top: 12px; width: 44px; height: 44px; }
  .feature-title { position: absolute; left: 59px; top: 0; font-family: "Merriweather", Georgia, serif; font-weight: 700; font-size: 17px; color: var(--ink); white-space: nowrap; }
  .feature-text { position: absolute; left: 59px; top: 29px; width: 280px; font-size: 13px; line-height: 21px; color: var(--muted); }

  .divider { position: absolute; left: 81px; top: 697px; width: 1038px; height: 1px; background: var(--line); }

  .binding-finder { position: absolute; top: 743px; left: 0; width: 1200px; height: 46px; }
  .select { position: absolute; top: 0; height: 46px; border: 1px solid var(--field-border); font-size: 13px; color: var(--muted); padding-left: 26px; line-height: 44px; }
  .select::after { content: "\02C7"; position: absolute; right: 26px; top: 1px; font-size: 12px; color: #999; }
  .find-btn { position: absolute; left: 992px; top: 0; width: 134px; height: 46px; background: var(--accent-soft); color: var(--white); font-size: 13px; font-weight: 700; display: flex; align-items: center; justify-content: center; gap: 8px; white-space: nowrap; }

  .bottom-rule { position: absolute; left: 0; top: 835px; width: 1200px; height: 4px; background: #f1f1f1; }
</style>
</head>
<body>
  <header class="site-header">
    <div class="brand">VELBRIN</div>
    <nav class="main-nav">
      <a class="is-active">START<span class="caret">&#9660;</span></a>
      <a>PRODUKTE<span class="caret">&#9660;</span></a>
      <a>BINDUNGEN<span class="caret">&#9660;</span></a>
      <a>RATGEBER<span class="caret">&#9660;</span></a>
      <a>KONTAKT</a>
    </nav>
    <div class="header-tools">
      <svg class="tool" style="left:987px;top:1px" viewBox="0 0 20 20" fill="none" stroke="#222" stroke-width="1.8"><circle cx="8.5" cy="8.5" r="6"/><line x1="13" y1="13" x2="18" y2="18"/></svg>
      <svg class="tool" style="left:1017px;top:1px" viewBox="0 0 20 20" fill="none" stroke="#222" stroke-width="1.8"><path d="M10 17 L3 10 A4 4 0 0 1 10 4.5 A4 4 0 0 1 17 10 Z"/></svg>
      <span class="tool-count" style="left:1035px;top:-7px">0</span>
      <svg class="tool" style="left:1063px;top:1px" viewBox="0 0 20 20" fill="none" stroke="#222" stroke-width="1.8"><rect x="3.5" y="6" width="13" height="12"/><path d="M7 6 V4 A3 3 0 0 1 13 4 V6"/></svg>
      <span class="tool-count" style="left:1081px;top:-7px">0</span>
      <svg class="tool" style="left:1108px;top:1px" viewBox="0 0 20 20" fill="none" stroke="#222" stroke-width="1.8"><circle cx="10" cy="6.5" r="4"/><path d="M3 18 A7 7 0 0 1 17 18"/></svg>
    </div>
  </header>

  <section class="hero">
    <div class="hero-photo" role="img" aria-label="Foto einer Hand, die mehrere Wandkalender mit Ring-Wire-Bindung in Violett, Orange und Magenta vor hellem Hintergrund hält">
      <div class="hero-product"></div>
    </div>
    <p class="hero-kicker">Erfahrung aus über 59 Jahren</p>
    <h1 class="hero-title">Service aus einer Hand –<br>Kompetenz verbindet!</h1>
    <div class="hero-cta">Jetzt entdecken</div>
  </section>
  <div class="slider-dots"><span></span><span class="is-current"></span><span></span></div>

  <section class="features">
    <div class="feature" style="left:81px">
      <svg class="feature-icon" viewBox="0 0 44 44" fill="none" stroke="#222" stroke-width="1.6"><path d="M6 26 H38 L34 36 H10 Z"/><rect x="12" y="16" width="20" height="10"/><rect x="18" y="9" width="8" height="7"/><path d="M4 39 Q9 36 14 39 T24 39 T34 39 T42 39"/></svg>
      <h3 class="feature-title">Kostenloser Versand</h3>
      <p class="feature-text">Große Auswahl an Kalenderbindungen und Zubehör.</p>
    </div>
    <div class="feature" style="left:438px">
      <svg class="feature-icon" viewBox="0 0 44 44" fill="none" stroke="#222" stroke-width="1.6"><ellipse cx="21" cy="26" rx="14" ry="10"/><circle cx="22" cy="9" r="5"/><path d="M35 24 H40 V29 H35"/><path d="M13 34 V40 M28 34 V40"/><circle cx="15" cy="24" r="1"/></svg>
      <h3 class="feature-title">Schnelle Lieferung</h3>
      <p class="feature-text">Gratis Versand und schnelle Lieferung Ihrer Bindungen.</p>
    </div>
    <div class="feature" style="left:795px">
      <svg class="feature-icon" viewBox="0 0 44 44" fill="none" stroke="#222" stroke-width="1.6"><circle cx="22" cy="22" r="18" stroke-dasharray="4 2"/><circle cx="22" cy="22" r="13"/><line x1="16" y1="28" x2="28" y2="16"/><circle cx="17" cy="17" r="2"/><circle cx="27" cy="27" r="2"/></svg>
      <h3 class="feature-title">Sonntagsrabatt</h3>
      <p class="feature-text">Jeden Sonntag Rabatt auf unsere beliebtesten Bindungen.</p>
    </div>
  </section>

  <div class="divider"></div>

  <section class="binding-finder">
    <div class="select" style="left:81px;width:429px">Alle Kategorien</div>
    <div class="select" style="left:537px;width:428px">Alle Bindungsarten</div>
    <div class="find-btn">
      <svg width="14" height="14" viewBox="0 0 20 20" fill="none" stroke="#fff" stroke-width="2.4"><circle cx="8.5" cy="8.5" r="6"/><line x1="13" y1="13" x2="18" y2="18"/></svg>
      Bindung finden
    </div>
  </section>

  <div class="bottom-rule"></div>
</body>
</html>
```